Personal training poster - 1200X900mm

Poster to promote my new personal training service at my gym. The poster will be printed and put into an aframe to be seen by people walking past my gym. It needs to be simple and eye catching with the text i have put in the must haves. The text and image should be the prominent parts of the design.

Target Market(s)

30-50 year old females

Industry/Entity Type

Fitness

Font styles to use
Sans Serif

Requirements
Must have
• my logo
• exercise graphic
• Must include the following text:
• Are you looking for a personal trainer? Our expert trainers can help you achieve you take your health and fitness back!
• Contact details:
• 1300452968
• info@brightmovegym.com.au
• Located under the Harbourview Club

```html
<!DOCTYPE html>
<html lang="en">
<head>
<meta charset="utf-8">
<title>BrightMove Gym – Personal Training Poster</title>
<link rel="stylesheet" href="https://fonts.googleapis.com/css2?family=Orbitron:wght@500&family=Questrial&family=Montserrat:wght@700&display=swap">
<style>
  :root {
    --page-bg: #e8eaeb;
    --poster-black: #0c0a0a;
    --poster-warm: #2a1a14;
    --skin-light: #c89a7c;
    --skin-mid: #9a6a50;
    --skin-dark: #3a241a;
    --copper: #c98a6c;
    --white: #ffffff;
  }
  * { margin: 0; padding: 0; box-sizing: border-box; }
  html, body {
    width: 1200px; height: 923px; overflow: hidden;
    background: var(--page-bg);
  }
  .poster {
    position: absolute; left: 20px; top: 26px;
    width: 1160px; height: 870px; overflow: hidden;
    background: radial-gradient(ellipse at 62% 55%, var(--poster-warm) 0%, var(--poster-black) 65%);
  }
  .photo { position: absolute; top: 0; height: 100%; }
  .photo--woman {
    left: 0; width: 320px;
    background: linear-gradient(90deg, var(--skin-dark) 0%, var(--skin-mid) 35%, var(--skin-light) 60%, var(--skin-mid) 85%, var(--poster-black) 100%);
  }
  .photo--man {
    left: 865px; width: 295px;
    background: linear-gradient(90deg, var(--poster-black) 0%, var(--skin-mid) 18%, var(--skin-light) 55%, var(--skin-mid) 85%, var(--skin-dark) 100%);
  }
  .headline {
    position: absolute; left: 320px; top: 22px;
    font-family: "Orbitron", sans-serif; font-weight: 500;
    font-size: 76px; line-height: 91px; letter-spacing: 6px;
    color: var(--white); text-transform: uppercase;
  }
  .intro {
    position: absolute; left: 357px; top: 410px;
    font-family: "Questrial", sans-serif;
    font-size: 42px; line-height: 52px; letter-spacing: 2.5px;
    color: var(--copper);
  }
  .contact { position: absolute; left: 350px; top: 686px; color: var(--white); font-family: "Questrial", sans-serif; }
  .contact__phone { font-family: "Montserrat", sans-serif; font-weight: 700; font-size: 48px; letter-spacing: 4px; line-height: 52px; }
  .contact__email { font-size: 38px; line-height: 48px; letter-spacing: 1px; }
  .contact__location { font-size: 44px; line-height: 54px; letter-spacing: 1.5px; }
  .brand {
    position: absolute; left: 110px; top: 712px; width: 210px;
    display: flex; flex-direction: column; align-items: center; gap: 12px;
    font-family: "Questrial", sans-serif; font-size: 26px; color: var(--white);
  }
  .brand__dot { width: 60px; height: 60px; border-radius: 50%; background: var(--white); }
</style>
</head>
<body>
  <main class="poster">
    <div class="photo photo--woman" role="img" aria-label="Photo of a fit woman's torso in a black sports top, cropped below the face"></div>
    <div class="photo photo--man" role="img" aria-label="Photo of a fit shirtless man's torso, cropped below the face"></div>

    <h1 class="headline">Looking<br>for a<br>personal<br>trainer?</h1>

    <p class="intro">Our expert trainers<br>can help you<br>achieve to take<br>your health &amp;<br>fitness back!</p>

    <div class="contact">
      <p class="contact__phone">1300452968</p>
      <p class="contact__email">info@brightmovegym.com.au</p>
      <p class="contact__location">Located under the Harbourview Club</p>
    </div>

    <div class="brand"><span class="brand__dot"></span><span class="brand__name">BrightMove Gym</span></div>
  </main>
</body>
</html>
```